New Stationary Design

Harcourt Electrics Ltd have acquired Brockhurst Catering Equipment Ltd. We will be retaining the Brockhurst Catering Equipment Ltd name and require new letter head, compliment slips & business card designs.

I have attached the existing Harcourt Electrics letterhead to show our current image/brand. I do not wish to change this substantially & imagine maybe a swap of colours from Red logo to Blue, and the title & footer bars maybe in Red. That said, I'm open to subtle changes in the overall design & to maybe modernise it and if we like them, we would probably ask the Designer to update the changes to reflect them on the Harcourt Electrics stationary as well.

We will be able to get some proper high def images for Catering equipment to include, but for the time being if desingers can use any standard stock images for initial presentation.

The logo will be printed onto a Red van so somehow we need to be able to modify it for that use.

Brockhurst Catering Equipment Ltd. Correspondence Address: 47 Lower Fenwick Road, Northampton. NN3 8QS. Tel 01604 738 902. Fax 01604 738 417. No website currently. Registered No: 05817264. Vat No: 481 3306 59. Company Registered Address: 22 Maplin Crescent, Leicester. LE2 7RD. We would also like to mention that we have Regional Service Centres also based in Leicester & Stockport.

Business Cards would be for;

Owen Hartley, Director. owen.hartley@brockhurstcatering-example.co.uk

Steven Pelham, Operations Manager. steven.pelham@brockhurstcatering-example.co.uk

Neil Booth, Service Manager. neil.booth@brockhurstcatering-example.co.uk

Martin Rowley, Business Development Manager. martin.rowley@brockhurstcatering-example.co.uk

We would also like the letter head to include the 'Fuel Guard' logo & our registration Number: To be confirmed. Also the Electrical Contractors logo & the words Wiring Installers Federation underneath so people know what it means. See www.wif-example.co.uk

Target Market(s)

Businesses who use Catering Equipment such as Cookers. fridges etc. Hence, Care Homes, Hospitals, Restaurants etc

Industry/Entity Type

Business

Requirements
Must have
• Resemblance to existing Harcourt Electrics brand, although maybe with some changes & modernisation.
Nice to have
• Could maybe have some 'icons' for the type of equipment we sell instead of photos. Ie Cookers, Ovens, Fridges, Microwaves, Dishwashers, as well as kithen cateringtabling, commercial extraction hoods etc.

```html
<!DOCTYPE html>
<html lang="en">
<head>
<meta charset="utf-8">
<title>Brockhurst Catering Equipment – Business Cards</title>
<link href="https://fonts.googleapis.com/css2?family=Arimo:wght@700&family=PT+Sans:wght@400;700&display=swap" rel="stylesheet">
<style>
  :root {
    --brand-blue: #2b3990;
    --brand-red: #ed1c24;
    --card-white: #ffffff;
    --backdrop: #ece7df;
    --icon-tint: #dfe3f3;
  }
  * { box-sizing: border-box; margin: 0; padding: 0; }
  html, body { width: 1200px; height: 1000px; overflow: hidden; }
  body { background: var(--backdrop); position: relative; font-family: "PT Sans", sans-serif; }

  .card { position: absolute; width: 516px; height: 289px; background: var(--card-white); box-shadow: 0 2px 6px rgba(0,0,0,.18); }
  .card--cover { left: 397px; top: 23px; height: 286px; background: var(--brand-red); }
  .card--owen { left: 31px; top: 364px; }
  .card--steven { left: 663px; top: 364px; }
  .card--neil { left: 31px; top: 696px; }
  .card--martin { left: 663px; top: 696px; }

  .brand-name { font-family: "PT Sans", sans-serif; font-weight: 700; color: var(--brand-blue); line-height: 1.05; }
  .card .brand-name { position: absolute; left: 32px; top: 20px; width: 200px; font-size: 25px; }
  .card--cover .brand-name { left: 116px; top: 44px; width: 290px; font-size: 38px; color: var(--card-white); text-align: center; }

  .federation { position: absolute; font-size: 10.5px; font-weight: 700; color: var(--brand-blue); }
  .card .federation { left: 32px; top: 104px; }
  .card--cover .federation { left: 0; width: 100%; top: 196px; text-align: center; font-size: 14px; font-weight: 400; }

  .equipment-strip { position: absolute; left: 116px; top: 237px; width: 278px; height: 63px; }

  .person { position: absolute; right: 37px; top: 98px; text-align: right; }
  .person-name { font-family: "Arimo", sans-serif; font-weight: 700; font-size: 32px; color: var(--brand-blue); line-height: 1.05; }
  .person-role { font-size: 18px; color: var(--brand-red); line-height: 1.05; }
  .person-role--small { font-size: 12.5px; }
  .person--compact .person-name { font-size: 29px; }

  .contact { position: absolute; left: 12px; top: 178px; font-size: 11.5px; line-height: 18px; color: var(--brand-blue); list-style: none; }
  .contact .label { color: var(--brand-red); }
  .contact .gap { margin-left: 12px; }

  .footer-band { position: absolute; left: 0; bottom: 0; width: 100%; height: 13px; background: var(--brand-red); }
</style>
</head>
<body>

<section class="card card--cover">
  <div class="brand-name">Brockhurst Catering Equipments</div>
  <p class="federation">Wiring Installers Federation</p>
  <svg class="equipment-strip" viewBox="0 0 278 63" role="img" aria-label="Row of catering equipment icons: dishwasher, fridge, extraction hood, microwave, cooker">
    <rect width="278" height="63" fill="var(--icon-tint)" opacity="0.35"/>
  </svg>
</section>

<section class="card card--owen">
  <div class="brand-name">Brockhurst Catering Equipments</div>
  <p class="federation">Wiring Installers Federation</p>
  <div class="person">
    <div class="person-name">Owen Hartley</div>
    <div class="person-role">Director</div>
  </div>
  <ul class="contact">
    <li><span class="label">Tel:</span> 01604 738 902 <span class="gap label">Fax:</span> 01604 738 417</li>
    <li><span class="label">Email:</span> hartley@harcourtelectrics-example.co.uk</li>
    <li><span class="label">Correspondence Address:</span> 47 Lower Fenwick Road, Northampton. NN3 8QS</li>
    <li><span class="label">Company Registered Address:</span> 22 Maplin Crescent, Leicester. LE2 7RD</li>
    <li>We have Regional Service Centres also based in Leicester &amp; Stockport.</li>
  </ul>
  <div class="footer-band"></div>
</section>

<section class="card card--steven">
  <div class="brand-name">Brockhurst Catering Equipments</div>
  <p class="federation">Wiring Installers Federation</p>
  <div class="person person--compact">
    <div class="person-name">Steven Pelham</div>
    <div class="person-role person-role--small">Operations Manager</div>
  </div>
  <ul class="contact">
    <li><span class="label">Tel:</span> 01604 738 902 <span class="gap label">Fax:</span> 01604 738 417</li>
    <li><span class="label">Email:</span> steven.pelham@brockhurstcatering-example.co.uk</li>
    <li><span class="label">Correspondence Address:</span> 47 Lower Fenwick Road, Northampton. NN3 8QS</li>
    <li><span class="label">Company Registered Address:</span> 22 Maplin Crescent, Leicester. LE2 7RD</li>
    <li>We have Regional Service Centres also based in Leicester &amp; Stockport.</li>
  </ul>
  <div class="footer-band"></div>
</section>

<section class="card card--neil">
  <div class="brand-name">Brockhurst Catering Equipments</div>
  <p class="federation">Wiring Installers Federation</p>
  <div class="person">
    <div class="person-name">Neil Booth</div>
    <div class="person-role">Service Manager</div>
  </div>
  <ul class="contact">
    <li><span class="label">Tel:</span> 01604 738 902 <span class="gap label">Fax:</span> 01604 738 417</li>
    <li><span class="label">Email:</span> neil.booth@brockhurstcatering-example.co.uk</li>
    <li><span class="label">Correspondence Address:</span> 47 Lower Fenwick Road, Northampton. NN3 8QS</li>
    <li><span class="label">Company Registered Address:</span> 22 Maplin Crescent, Leicester. LE2 7RD</li>
    <li>We have Regional Service Centres also based in Leicester &amp; Stockport.</li>
  </ul>
  <div class="footer-band"></div>
</section>

<section class="card card--martin">
  <div class="brand-name">Brockhurst Catering Equipments</div>
  <p class="federation">Wiring Installers Federation</p>
  <div class="person person--compact">
    <div class="person-name">Martin Rowley</div>
    <div class="person-role person-role--small">Business Development Manager</div>
  </div>
  <ul class="contact">
    <li><span class="label">Tel:</span> 01604 738 902 <span class="gap label">Fax:</span> 01604 738 417</li>
    <li><span class="label">Email:</span> martin.rowley@brockhurstcatering-example.co.uk</li>
    <li><span class="label">Correspondence Address:</span> 47 Lower Fenwick Road, Northampton. NN3 8QS</li>
    <li><span class="label">Company Registered Address:</span> 22 Maplin Crescent, Leicester. LE2 7RD</li>
    <li>We have Regional Service Centres also based in Leicester &amp; Stockport.</li>
  </ul>
  <div class="footer-band"></div>
</section>

</body>
</html>
```